Foldable AirLink Headphone Packaging Design

We would like a window box style packaging design for our Foldable AirLink Headphone.

We want to use the packaging for 4-5 of our AirLink headphone series (enclosed picture of the headphones for reference) and hence we would not like to put any product pictures on the packaging.
Material: E-Flute Paper box
Type: Window Box style
Design features we prefer: Colorful, creative, trendy, High tech.
Requirement: AI file is preferred
Size of Packaging: 170 (L) x 120 (W) x 200 (H) mm

Enclosed are a detailed description along with competitor designs for your reference.

Any further questions, please feel free to ask.

Target Market(s)

25-35 year olds

Industry/Entity Type

Electronics

Colors

Designer to choose colors to be used in the design.

Requirements
Must have
• Trendy Design

```html
<!DOCTYPE html>
<html lang="en">
<head>
<meta charset="utf-8">
<title>Foldable AirLink Headphone – Box Dieline</title>
<link href="https://fonts.googleapis.com/css2?family=Saira+Condensed:wght@500;700;800&family=Roboto+Condensed:wght@400;700&display=swap" rel="stylesheet">
<style>
  :root {
    --paper: #ffffff;
    --board: #231f20;
    --ink: #ffffff;
    --ink-soft: #d8d8d8;
    --glow: #2fd6f0;
    --glow-deep: #0c6f84;
    --fold: #8a8a8a;
    --window: #ffffff;
    --brand-dot: #1f78d1;
  }
  * { margin: 0; padding: 0; box-sizing: border-box; }
  html, body { width: 1200px; height: 1000px; overflow: hidden; background: var(--paper); }
  .canvas { position: relative; width: 1200px; height: 1000px; }

  .panel { position: absolute; background: var(--board); overflow: hidden; }
  .flap-top { left: 212px; top: 221px; width: 215px; height: 152px; }
  .flap-bottom { left: 212px; top: 627px; width: 215px; height: 151px; }
  .body-strip { left: 60px; top: 373px; width: 735px; height: 254px; }

  .glow-top {
    position: absolute; left: 300px; top: -60px; width: 330px; height: 150px;
    background: radial-gradient(ellipse at center, rgba(47,214,240,.5) 0%, rgba(12,111,132,.22) 35%, transparent 70%);
  }
  .glow-bottom {
    position: absolute; left: 330px; top: 180px; width: 280px; height: 110px;
    background: radial-gradient(ellipse at center, rgba(12,111,132,.45) 0%, transparent 70%);
  }
  .glow-line {
    position: absolute; left: 0; top: 172px; width: 735px; height: 2px;
    background: var(--glow); box-shadow: 0 0 6px var(--glow), 0 0 14px var(--glow-deep);
  }
  .fold { position: absolute; top: 0; width: 1px; height: 254px; background: rgba(255,255,255,.08); }

  .window { position: absolute; top: 41px; height: 171px; background: var(--window); }
  .window-a { left: 260px; width: 107px; }
  .window-b { left: 368px; width: 151px; }
  .window-c { left: 520px; width: 106px; }
  .window-crease { position: absolute; top: 41px; width: 1px; height: 171px; background: var(--fold); }

  .title {
    position: absolute; top: 8px;
    font-family: 'Saira Condensed', sans-serif; font-style: italic; font-weight: 800;
    font-size: 18px; line-height: 24px; color: var(--ink); white-space: nowrap;
  }
  .brand {
    position: absolute; top: 48px; display: flex; align-items: center; gap: 3px;
    font-family: 'Roboto Condensed', sans-serif; font-weight: 700; font-size: 12px; line-height: 14px; color: var(--ink);
  }
  .brand-dot { width: 11px; height: 11px; border-radius: 50%; background: var(--brand-dot); }
  .features {
    position: absolute; top: 80px; list-style: none;
    font-family: 'Saira Condensed', sans-serif; font-style: italic; font-weight: 700;
    font-size: 5.5px; color: var(--ink); line-height: 10.5px; white-space: nowrap;
  }
  .features li { display: flex; align-items: center; gap: 4px; }
  .features svg { width: 6px; height: 6px; flex: none; }

  .wave { position: absolute; top: 135px; height: 80px;
    background: radial-gradient(ellipse at center, rgba(47,214,240,.55) 0%, rgba(12,111,132,.28) 45%, transparent 75%); }

  .specs {
    position: absolute; left: 37px; top: 42px;
    font-family: 'Roboto Condensed', sans-serif; font-size: 4.6px; line-height: 10.2px; color: var(--ink-soft);
  }
  .specs h4 { font-weight: 700; color: var(--ink); font-size: 5px; }

  .label {
    position: absolute; left: 8px; top: 193px; width: 62px; height: 34px; background: var(--ink);
    font-family: 'Roboto Condensed', sans-serif; font-size: 4px; color: #222; padding: 7px 6px; line-height: 7px;
  }
  .marks { position: absolute; left: 88px; top: 214px; display: grid; grid-template-columns: repeat(4, 7px); gap: 4px 6px; }
  .mark { width: 7px; height: 7px; border: 1px solid var(--ink); border-radius: 50%; }
</style>
</head>
<body>
<div class="canvas">
  <div class="panel flap-top"></div>
  <div class="panel flap-bottom"></div>

  <div class="panel body-strip">
    <div class="glow-top"></div>
    <div class="glow-bottom"></div>
    <div class="glow-line"></div>

    <div class="fold" style="left:152px"></div>
    <div class="fold" style="left:519px"></div>

    <div class="specs">
      <h4>Specification:</h4>
      <p>Wireless Version: 5.0</p>
      <p>Wireless Playback Duration: 10-12 h</p>
      <p>Standby Time: 80 h</p>
      <p>Wireless Range: 10 m</p>
      <p>Impedance: 32 Ω</p>
      <p>Sound Pressure Level: 108dB ± 3dB</p>
      <p>Frequency Response: 20-20kHz</p>
      <p>Plug Type: 3.5mm Stereo Detachable</p>
      <p>Driver Unit: 40mm</p>
    </div>
    <div class="label">MODEL HP-01<br>MADE IN CHINA</div>
    <div class="marks">
      <span class="mark"></span><span class="mark"></span><span class="mark"></span><span class="mark"></span>
      <span class="mark"></span><span class="mark"></span><span class="mark"></span><span class="mark"></span>
    </div>

    <h2 class="title" style="left:168px">Foldable AirLink Headphone</h2>
    <div class="brand" style="left:162px"><span class="brand-dot"></span>AirLink</div>
    <ul class="features" style="left:162px">
      <li><svg viewBox="0 0 6 6"><path d="M1 4V3a2 2 0 0 1 4 0v1" fill="none" stroke="#fff" stroke-width=".8"/></svg>airlink v5</li>
      <li><svg viewBox="0 0 6 6"><path d="M1 4V3a2 2 0 0 1 4 0v1" fill="none" stroke="#fff" stroke-width=".8"/></svg>foldable and portable</li>
      <li><svg viewBox="0 0 6 6"><path d="M1 4V3a2 2 0 0 1 4 0v1" fill="none" stroke="#fff" stroke-width=".8"/></svg>exceptional sound quality</li>
      <li><svg viewBox="0 0 6 6"><path d="M1 4V3a2 2 0 0 1 4 0v1" fill="none" stroke="#fff" stroke-width=".8"/></svg>dual mode wireless or wired connectivity</li>
      <li><svg viewBox="0 0 6 6"><path d="M1 4V3a2 2 0 0 1 4 0v1" fill="none" stroke="#fff" stroke-width=".8"/></svg>adjustable headband</li>
    </ul>
    <div class="wave" role="img" aria-label="Glowing cyan sound wave graphic" style="left:195px;width:70px"></div>

    <div class="window window-a"></div>
    <div class="window window-b"></div>
    <div class="window window-c"></div>
    <div class="window-crease" style="left:367px"></div>
    <div class="window-crease" style="left:519px"></div>

    <h2 class="title" style="left:532px">Foldable AirLink Headphone</h2>
    <div class="brand" style="left:637px"><span class="brand-dot"></span>AirLink</div>
    <ul class="features" style="left:637px">
      <li><svg viewBox="0 0 6 6"><path d="M1 4V3a2 2 0 0 1 4 0v1" fill="none" stroke="#fff" stroke-width=".8"/></svg>airlink v5</li>
      <li><svg viewBox="0 0 6 6"><path d="M1 4V3a2 2 0 0 1 4 0v1" fill="none" stroke="#fff" stroke-width=".8"/></svg>foldable and portable</li>
      <li><svg viewBox="0 0 6 6"><path d="M1 4V3a2 2 0 0 1 4 0v1" fill="none" stroke="#fff" stroke-width=".8"/></svg>exceptional sound quality</li>
      <li><svg viewBox="0 0 6 6"><path d="M1 4V3a2 2 0 0 1 4 0v1" fill="none" stroke="#fff" stroke-width=".8"/></svg>dual mode wireless or wired connectivity</li>
      <li><svg viewBox="0 0 6 6"><path d="M1 4V3a2 2 0 0 1 4 0v1" fill="none" stroke="#fff" stroke-width=".8"/></svg>adjustable headband</li>
    </ul>
    <div class="wave" role="img" aria-label="Glowing cyan sound wave graphic" style="left:626px;width:60px"></div>
  </div>
</div>
</body>
</html>
```